Marlene Business Card

My wife is going to start her own business with renting holiday appartments to tourists. She needs a design for a new business card... and a new web site.
Look at Roomvesta "Ruhezeit am Birkenteich"

Target Market(s)

Give business card to prospects at any situation

Contact Information for Business Card

not sure what this means

Font styles to use
Script

Colors
fec41a
fee18a

Requirements
Must have
• My wife's handwriting is difficult to read:
Entspannen - Loslassen - Auftanken
Marlene & der Birkenteich
Urlaub an einem besonderen Ort
Marlene Brökel
Gartenpfad 7
17489 Alt Medow
info@marlene-broekel.de
www.birkenteich.net
Nice to have
• Beige background
Font like handwriting

```html
<!DOCTYPE html>
<html lang="de">
<head>
<meta charset="utf-8">
<title>Marlene &amp; der Birkenteich – Visitenkarte</title>
<link rel="stylesheet" href="https://fonts.googleapis.com/css2?family=Caveat+Brush&family=Caveat:wght@500&family=Jost:wght@300&display=swap">
<style>
  :root {
    --backdrop: #6f6157;
    --card-white: #ffffff;
    --taupe: #ad9a8b;
    --ink: #2b2b2b;
    --accent: #a88a76;
  }
  html, body {
    margin: 0;
    padding: 0;
    width: 892px;
    height: 1200px;
    overflow: hidden;
    background: var(--backdrop);
  }
  .canvas {
    position: relative;
    width: 892px;
    height: 1200px;
  }
  .card {
    position: absolute;
    left: 60px;
    width: 782px;
    height: 506px;
    border-radius: 44px;
    box-shadow: 10px 14px 22px rgba(40, 30, 24, 0.45);
    text-align: center;
  }
  .card--front { top: 57px; background: var(--card-white); }
  .card--back { top: 628px; background: var(--taupe); }

  .line {
    position: absolute;
    left: 0;
    right: 0;
    margin: 0;
    white-space: nowrap;
    line-height: 1;
  }
  .brand-name,
  .brand-tagline {
    font-family: "Caveat Brush", cursive;
    color: var(--taupe);
  }
  .brand-name { top: 118px; font-size: 50px; }
  .brand-tagline { top: 178px; font-size: 44px; }

  .divider {
    position: absolute;
    top: 286px;
    left: 356px;
    width: 70px;
    height: 1px;
    background: var(--accent);
  }

  .contact-row {
    top: 333px;
    font-family: "Jost", sans-serif;
    font-weight: 300;
    font-size: 17px;
    color: var(--ink);
  }
  .contact-row .sep {
    display: inline-block;
    width: 2px;
    height: 17px;
    margin: 0 12px;
    vertical-align: -2px;
    background: var(--accent);
  }
  .address {
    font-family: "Jost", sans-serif;
    font-weight: 300;
    font-size: 18px;
    color: var(--ink);
  }
  .address--street { top: 377px; }
  .address--city { top: 401px; }

  .back-line {
    font-family: "Caveat", cursive;
    font-weight: 500;
    font-size: 42px;
    color: var(--card-white);
  }
  .back-line--motto { top: 175px; }
  .back-line--name { top: 234px; }
  .back-line--tagline { top: 292px; }
</style>
</head>
<body>
  <main class="canvas">
    <section class="card card--front" aria-label="Vorderseite">
      <h1 class="line brand-name">Marlene &amp; der Birkenteich</h1>
      <p class="line brand-tagline">Urlaub an einem besonderen Ort</p>
      <div class="divider"></div>
      <p class="line contact-row">+49 151 408 336 19<span class="sep"></span>www.birkenteich.net<span class="sep"></span>info@marlene-broekel.de</p>
      <p class="line address address--street">Gartenpfad 7, 17489</p>
      <p class="line address address--city">Alt Medow, Germany</p>
    </section>

    <section class="card card--back" aria-label="Rückseite">
      <p class="line back-line back-line--motto">Entspannen - Loslassen - Auftanken</p>
      <p class="line back-line back-line--name">Marlene &amp; der Birkenteich</p>
      <p class="line back-line back-line--tagline">Urlaub an einem besonderen Ort</p>
    </section>
  </main>
</body>
</html>
```